Qualifying Builders Questionnaire

We need a questionnaire designed to send out to potential clients with qualifying questions

Industry/Entity Type

Building

Colors

Designer to choose colors to be used in the design.

```html
<!DOCTYPE html>
<html lang="en">
<head>
<meta charset="utf-8">
<title>Harbour Lane Homes – Client Questionnaire</title>
<link rel="stylesheet" href="https://fonts.googleapis.com/css2?family=Roboto:wght@300;400;500;700&display=swap">
<style>
  :root {
    --brand-red: #ec2229;
    --brand-dark: #3a3a3a;
    --page-grey: #a6a5a5;
    --topbar: #f1f0f0;
    --panel: #f7f7f7;
    --panel-line: #e6e6e6;
    --field-line: #cfcfcf;
    --text: #4a4a4a;
    --muted: #8a8a8a;
    --heading: #555;
    --link: #1ea7e1;
    --white: #ffffff;
  }
  * { box-sizing: border-box; margin: 0; padding: 0; }
  html, body { width: 1200px; height: 3827px; overflow: hidden; }
  body {
    position: relative;
    background: var(--page-grey);
    font-family: "Roboto", Arial, sans-serif;
    color: var(--text);
  }
  .topbar {
    position: absolute; left: 0; top: 0; width: 1200px; height: 112px;
    background: var(--topbar);
    font-size: 21px; color: #222;
    display: flex; align-items: center; justify-content: center;
  }
  .topbar a { color: #222; text-decoration: underline; margin-left: 8px; }
  .topbar-rule { position: absolute; left: 0; top: 112px; width: 1200px; height: 11px; background: #111; }

  .sheet { position: absolute; left: 148px; top: 123px; width: 904px; height: 3704px; background: var(--white); }
  .masthead { position: absolute; left: 148px; top: 123px; width: 904px; height: 342px; }
  .masthead svg { position: absolute; left: 0; top: 0; }
  .brand {
    position: absolute; left: 0; top: 30px; width: 904px; text-align: center;
    color: var(--white); font-weight: 700;
  }
  .brand-mark { display: block; width: 80px; height: 80px; margin: 0 auto 60px; background: var(--white); }
  .brand-name { display: block; font-size: 48px; letter-spacing: 2px; line-height: 1; }
  .brand-sub { display: block; font-size: 22px; letter-spacing: 8px; margin-top: 8px; line-height: 1; }

  .intro {
    position: absolute; left: 148px; top: 500px; width: 904px; text-align: center;
    font-weight: 300; font-size: 51px; line-height: 62px; color: var(--heading);
  }

  .section-bar {
    position: absolute; left: 179px; width: 842px; height: 55px;
    background: var(--brand-red); color: var(--white);
    font-weight: 500; font-size: 30px; letter-spacing: 1px;
    padding-left: 26px; display: flex; align-items: center;
  }
  .panel {
    position: absolute; left: 179px; width: 842px;
    background: var(--panel); border: 2px solid var(--panel-line); border-top: 0;
  }
  .field {
    position: absolute; height: 51px; background: var(--white);
    border: 2px solid var(--field-line); font-size: 19px; color: var(--muted);
    padding: 12px 14px;
  }
  .field.tall { height: 133px; }

  .q-title { position: absolute; left: 204px; font-size: 22px; font-weight: 700; color: #333; }
  .q-note { position: absolute; left: 204px; font-size: 22px; color: var(--muted); line-height: 30px; }
  .q-note a { color: var(--link); text-decoration: none; }
  .q-hint { position: absolute; left: 204px; font-size: 19px; color: var(--brand-red); text-decoration: underline; }

  .check { position: absolute; display: flex; align-items: center; font-size: 19px; color: var(--text); white-space: nowrap; }
  .check .box {
    width: 30px; height: 30px; background: var(--white);
    border: 2px solid var(--field-line); margin-right: 16px; flex: none;
  }
  .check-list { position: absolute; left: 204px; list-style: none; }
  .check-list li { height: 66.4px; display: flex; align-items: center; font-size: 19px; }
  .check-list .box { width: 30px; height: 30px; background: var(--white); border: 2px solid var(--field-line); margin-right: 16px; flex: none; }
</style>
</head>
<body>
  <div class="topbar">Don't see this email properly? <a href="#">View in web browser</a></div>
  <div class="topbar-rule"></div>

  <div class="sheet"></div>

  <header class="masthead">
    <svg width="904" height="342" viewBox="0 0 904 342" aria-hidden="true">
      <polygon points="0,0 904,0 904,262 452,342 0,262" fill="var(--brand-dark)"/>
      <polygon points="0,0 904,0 904,243 452,311 0,243" fill="var(--brand-red)"/>
    </svg>
    <div class="brand">
      <span class="brand-mark"></span>
      <span class="brand-name">HARBOUR LANE</span>
      <span class="brand-sub">HOMES (NSW)</span>
    </div>
  </header>

  <h1 class="intro">Please fill up the question<br>and send to us.</h1>

  <div class="section-bar" style="top:679px">CLIENT DETAILS *</div>
  <section class="panel" style="top:734px;height:734px"></section>
  <div class="field" style="left:204px;top:761px;width:792px">* Name</div>
  <div class="field" style="left:204px;top:830px;width:388px">* Phone</div>
  <div class="field" style="left:608px;top:830px;width:388px">Mobile</div>
  <div class="field" style="left:204px;top:901px;width:792px">* Email</div>
  <div class="field tall" style="left:204px;top:973px;width:792px">* Mailing Address</div>
  <div class="q-title" style="top:1138px;left:218px;font-size:21px">* Land or property details:</div>
  <div class="check" style="left:204px;top:1180px"><span class="box"></span>Same as mailing address</div>
  <div class="field" style="left:204px;top:1241px;width:388px">Lot number (if applicable):</div>
  <div class="field" style="left:608px;top:1241px;width:388px">Unit number</div>
  <div class="field" style="left:204px;top:1310px;width:388px">Street number</div>
  <div class="field" style="left:608px;top:1310px;width:388px">Street name</div>
  <div class="field" style="left:204px;top:1381px;width:388px">Suburb:</div>
  <div class="field" style="left:608px;top:1381px;width:388px">Estate name (if applicable) :</div>

  <div class="section-bar" style="top:1501px">CLIENT ANALYSIS QUESTIONNAIRE *</div>
  <section class="panel" style="top:1555px;height:2272px"></section>

  <div class="q-title" style="top:1578px">How did you come across us?</div>
  <div class="check" style="left:204px;top:1639px"><span class="box"></span>Search-website</div>
  <div class="check" style="left:414px;top:1639px"><span class="box"></span>Site signage</div>
  <div class="check" style="left:597px;top:1639px"><span class="box"></span>Ute signage</div>
  <div class="check" style="left:771px;top:1639px"><span class="box"></span>Email marketing</div>
  <div class="check" style="left:204px;top:1706px"><span class="box"></span>Flyer</div>
  <div class="check" style="left:416px;top:1706px"><span class="box"></span>Business card</div>
  <div class="check" style="left:597px;top:1706px"><span class="box"></span>Past client</div>
  <div class="check" style="left:771px;top:1706px"><span class="box"></span>Referral</div>
  <div class="check" style="left:204px;top:1772px"><span class="box"></span>Other:&nbsp; What</div>

  <div class="q-title" style="top:1848px">What does you enquiry relate to? *</div>
  <ul class="check-list" style="top:1890px">
    <li><span class="box"></span>Passive house design, build &amp; certification</li>
    <li><span class="box"></span>New home design &amp; build with passive elements</li>
    <li><span class="box"></span>Extension with passive elements</li>
    <li><span class="box"></span>Renovation with passive elements</li>
    <li><span class="box"></span>Conventional new home design and build</li>
    <li><span class="box"></span>Conventional extension</li>
    <li><span class="box"></span>Conventional renovation</li>
    <li><span class="box"></span>Other:</li>
  </ul>

  <div class="q-title" style="top:2456px">Have you obtained any plans or documentation for your project? *</div>
  <div class="q-note" style="top:2494px">If you are unsure of your requirements please visit the Building Standards Office<br><a href="#">@ www.buildingstandards.example.org</a></div>
  <div class="check" style="left:204px;top:2582px"><span class="box"></span>Yes</div>
  <div class="check" style="left:324px;top:2582px"><span class="box"></span>No</div>
  <div class="q-hint" style="top:2656px">If yes, please select from the following list to indicate what you have</div>

  <ul class="check-list" style="top:2694px">
    <li><span class="box"></span>Concept design(s)</li>
    <li><span class="box"></span>Planning permit</li>
    <li><span class="box"></span>Site feature and level survey</li>
    <li><span class="box"></span>Title boundary re-establishment survey( required if you wish to build to the boundary)</li>
    <li><span class="box"></span>Engineering computations</li>
    <li><span class="box"></span>Geotechnical report</li>
    <li><span class="box"></span>Drainage plans</li>
    <li><span class="box"></span>Sewer details</li>
    <li><span class="box"></span>Stormwater/landfill information</li>
    <li><span class="box"></span>Energy rating report</li>
    <li><span class="box"></span>Electrical plan</li>
    <li><span class="box"></span>Internal joinery documentation</li>
    <li><span class="box"></span>Window schedule</li>
    <li><span class="box"></span>I have no idea what I have been given</li>
    <li><span class="box"></span>Other</li>
  </ul>
</body>
</html>
```